Private School social media templates / ads

We are a school in South Australia -around 40kms south of Adelaide. We have 2 campuses and need fresh looks for our social media advertising.

These ads need to be designed so that our team can use them and change headings as needed or images. Ideally, PSD files or InDesign files work best.

We would need you to use stock images initially so that we can then add student photos to the ads or, if you have a different suggestion we need to come up with fresh ideas to get our message across. Here is a bit of background:

A private Christian school - one campus in Morphett Vale in the south of Adelaide and our second campus in Aldinga - we are a smaller school compared to many larger ones, so our main focus of marketing is a messages along the lines of:
- Academic Excellence (see additional notes below on this topic)
- Respect and Values and Faith
- Student focused approach to teaching - smaller class sizes means no student is left behinid.

Parents give us feedback saying they like a school with good values and one that teaches respect but also is respectful. We have a strong no-bullying policy and our academics are excellent when comparing TREVOK data.

Note - Academic Excellence.
One thing I've tried to communicate is that academic excellence is not just about getting high marks, instead, it is about encouraging students to be the best they can be. So in the past headings like - Give your Child a Great Start - and similar have worked well. Also, a strong point is - At Kestrel Ridge, your child is never just a number, but a valued part of our community.

These are some starting points. One thing I'd like to encourage is creativity - almost every school uses the same old style of advertising - a pic of 1 or 2 students and a heading like - Principals Tours - book now.

We need to stand out from the crowd when we advertise our tours.

The main focus is to increase enrolment numbers. We have a good quality CRM running so all enquiries go through a Funnel System.

I've included logos and brand documents - however, we are happy to move away from the fonts and be a bit creative with colours and tones we use.

Also, I have included a series we called -Crayons and Comets - where we created tech/space-themed ads showing where students could be in the future. This campaign ran for 2 years now and we need a fresh look with this sort of impact.

Target Market(s)

Primarily female aged 25-49

Industry/Entity Type

education - private school adelaide

Font styles to use
Sans Serif
Other font styles liked:
• Roboto is currently used but open to suggestions. Do not use Mutal Feelings font.

Requirements
Must have
• brand and promote school and school principal tours
Nice to have
• In our brand guide, there are our colours, ideally using those colors and tones for design
Should not have
• no generic ad designs - what I mean is a picture of a smiling student with the heading - Principal's Tours now on

```html
<!DOCTYPE html>
<html lang="en">
<head>
<meta charset="utf-8">
<title>Kestrel Ridge Christian College – Social Ad Series</title>
<link rel="stylesheet" href="https://fonts.googleapis.com/css2?family=Archivo+Black&family=Kumbh+Sans:wght@600;800&family=League+Gothic:wdth@75..100&display=swap">
<style>
  :root{
    --board-top:#303030;
    --board-bottom:#7c7c7c;
    --sun:#ffc63c;
    --sun-deep:#f5ae22;
    --sky:#1f9be0;
    --sky-deep:#1783c9;
    --flame:#e63b2e;
    --flame-deep:#c9251d;
    --lilac:#a87cba;
    --lilac-deep:#8f61a6;
    --brand-blue:#1c7fc9;
    --brand-red:#e5262a;
    --white:#ffffff;
    --ink-shadow:#0d3f72;
  }
  *{margin:0;padding:0;box-sizing:border-box}
  html,body{width:824px;height:1200px;overflow:hidden}
  body{
    position:relative;
    background:linear-gradient(180deg,var(--board-top) 0%,var(--board-bottom) 100%);
    font-family:"Kumbh Sans",sans-serif;
  }
  .ad{position:absolute;width:336px;height:336px;overflow:hidden}
  .ad--values{left:51px;top:39px;background:var(--sun)}
  .ad--happy{left:412px;top:39px;background:var(--sky)}
  .ad--faith{left:51px;top:417px;background:var(--flame)}
  .ad--academic{left:412px;top:417px;background:var(--sky)}
  .ad--number{left:51px;top:800px;background:var(--lilac)}
  .ad--standout{left:412px;top:800px;background:var(--flame)}

  .photo{position:absolute}
  .headline{
    position:absolute;color:var(--white);
    font-family:"League Gothic",sans-serif;font-stretch:75%;
    text-transform:uppercase;white-space:nowrap;line-height:.82;
    transform:scaleY(1.32);transform-origin:top left;
  }
  .caption{
    position:absolute;font-weight:800;font-variant:small-caps;
    text-transform:lowercase;letter-spacing:.2px;line-height:1.05;
  }
  .wordmark{
    color:var(--brand-blue);font-family:"Kumbh Sans",sans-serif;
    font-weight:600;line-height:1.02;white-space:nowrap;
  }
  .wordmark-dot{display:inline-block;background:var(--brand-blue);border-radius:50%}
  .cta{
    position:absolute;border-radius:20px;text-align:center;
    font-weight:800;font-variant:small-caps;text-transform:lowercase;letter-spacing:.6px;
  }

  /* Values */
  .ad--values .photo{left:0;top:0;width:208px;height:336px;
    background:radial-gradient(ellipse at 50% 45%,#ffe3a0 0%,#f3b93c 55%,var(--sun-deep) 100%)}
  .ad--values .brand-tab{position:absolute;right:0;top:0;width:175px;height:49px;
    background:var(--white);border-bottom-left-radius:26px;display:flex;align-items:center;gap:6px;padding-left:16px}
  .ad--values .wordmark{font-size:13px}
  .ad--values .wordmark-dot{width:18px;height:18px}
  .ad--values .headline{right:9px;top:60px;font-size:76px;transform-origin:top right}
  .ad--values .caption{right:11px;top:144px;text-align:right;color:var(--brand-red);font-size:12.5px}
  .ad--values .cta{left:218px;top:199px;width:109px;height:20px;line-height:20px;
    background:var(--brand-red);color:var(--white);font-size:12px}

  /* Happy students */
  .ad--happy .brand-tab{position:absolute;left:75px;top:0;width:181px;height:40px;background:var(--white);
    border-radius:0 0 22px 22px;display:flex;align-items:center;justify-content:center;gap:6px}
  .ad--happy .wordmark{font-size:12px}
  .ad--happy .wordmark-dot{width:16px;height:16px}
  .ad--happy .big-title{position:absolute;left:0;top:51px;width:336px;text-align:center;color:var(--white);
    font-family:"Archivo Black",sans-serif;font-size:27px;line-height:.98;letter-spacing:.5px;
    text-shadow:0 0 3px var(--ink-shadow),1px 1px 0 var(--ink-shadow),-1px -1px 0 var(--ink-shadow)}
  .ad--happy .caption{left:0;top:118px;width:336px;text-align:center;color:var(--white);font-size:13px;
    text-shadow:0 0 2px var(--ink-shadow)}
  .ad--happy .photo{left:0;top:190px;width:336px;height:146px;
    background:linear-gradient(180deg,var(--sky) 0%,#3f8fc9 45%,#2566a8 100%)}
  .ad--happy .cta{left:110px;top:310px;width:124px;height:17px;line-height:17px;
    background:var(--white);color:var(--brand-blue);font-size:10.5px}

  /* Faith & focus */
  .ad--faith .photo{left:140px;top:15px;width:196px;height:321px;
    background:radial-gradient(ellipse at 55% 40%,#f2c8a8 0%,#f1b13a 45%,#3e5f86 85%,var(--flame-deep) 100%)}
  .ad--faith .headline{left:17px;top:26px;font-size:82px;line-height:.8}
  .ad--faith .caption{left:18px;top:212px;color:var(--white);font-size:15px}
  .ad--faith .brand-box{position:absolute;left:18px;top:271px;width:92px;height:65px;background:var(--white);
    display:flex;flex-direction:column;align-items:center;justify-content:center;gap:4px;text-align:center}
  .ad--faith .wordmark{font-size:10px}
  .ad--faith .wordmark-dot{width:18px;height:18px}

  /* Academic excellence */
  .ad--academic .sun-band{position:absolute;left:0;top:0;width:336px;height:176px;background:var(--sun)}
  .ad--academic .photo{left:104px;top:26px;width:232px;height:310px;
    background:radial-gradient(ellipse at 60% 35%,#f2cdb0 0%,#e9a04a 40%,#3c5d86 80%,var(--sky-deep) 100%);
    border-radius:60px 40px 0 0}
  .ad--academic .headline{left:10px;top:12px;font-size:66px;line-height:.78;transform:scaleY(1.28)}
  .ad--academic .caption{left:11px;top:184px;color:var(--white);font-size:13px}
  .ad--academic .brand-line{position:absolute;left:11px;top:301px;display:flex;align-items:center;gap:5px}
  .ad--academic .wordmark{font-size:9.5px;color:var(--white)}
  .ad--academic .wordmark-dot{width:16px;height:16px;background:var(--white)}

  /* Just a number */
  .ad--number .photo{left:0;top:0;width:217px;height:336px;
    background:linear-gradient(180deg,#c9a98e 0%,#e8c2a4 35%,#f4f4f4 70%,#ececec 100%)}
  .ad--number .headline{right:12px;top:22px;text-align:right;font-size:37px;line-height:.84;transform-origin:top right}
  .ad--number .caption{right:11px;top:156px;text-align:right;color:var(--white);font-size:11.5px;line-height:1.08}
  .ad--number .brand-tab{position:absolute;right:0;top:300px;width:119px;height:36px;background:var(--white);
    border-top-left-radius:16px;display:flex;align-items:center;justify-content:center;gap:5px}
  .ad--number .wordmark{font-size:9px}
  .ad--number .wordmark-dot{width:15px;height:15px}

  /* Stand out */
  .ad--standout .glow{position:absolute;left:118px;top:0;width:100px;height:336px;
    background:linear-gradient(180deg,rgba(255,255,255,.35) 0%,rgba(255,255,255,.08) 60%,rgba(255,255,255,0) 100%)}
  .ad--standout .photo{left:0;top:136px;width:336px;height:200px;
    background:radial-gradient(ellipse at 50% 55%,#f6c6b3 0%,#ee86b5 30%,#b8302a 65%,var(--flame-deep) 100%)}
  .ad--standout .headline{left:18px;top:12px;font-size:91px;letter-spacing:-.5px}
  .ad--standout .caption{left:0;top:114px;width:336px;text-align:center;color:var(--white);font-size:20px}
  .ad--standout .brand-tab{position:absolute;left:0;top:282px;width:84px;height:54px;background:var(--white);
    border-top-right-radius:16px;display:flex;flex-direction:column;align-items:center;justify-content:center;gap:3px;text-align:center}
  .ad--standout .wordmark{font-size:9px}
  .ad--standout .wordmark-dot{width:15px;height:15px}
</style>
</head>
<body>

<section class="ad ad--values">
  <div class="photo" role="img" aria-label="Child in a blazer and red tie standing inside a chalk-drawn red rocket, looking upward"></div>
  <div class="brand-tab"><span class="wordmark-dot"></span><span class="wordmark">Kestrel Ridge<br>Christian College</span></div>
  <h2 class="headline">Values</h2>
  <p class="caption">Helping your child<br>navigate &amp; prepare<br>for their future</p>
  <div class="cta">Book Now</div>
</section>

<section class="ad ad--happy">
  <div class="brand-tab"><span class="wordmark-dot"></span><span class="wordmark">Kestrel Ridge<br>Christian College</span></div>
  <h2 class="big-title">HAPPY STUDENTS<br>ENJOY LEARNING</h2>
  <p class="caption">At Kestrel Ridge you child is valued,<br>respected and cared for.</p>
  <div class="photo" role="img" aria-label="Five young students sitting cross-legged in a row holding open colourful books"></div>
  <div class="cta">Book Now</div>
</section>

<section class="ad ad--faith">
  <div class="photo" role="img" aria-label="Smiling schoolgirl in a yellow top and denim overalls carrying a blue backpack"></div>
  <h2 class="headline">Faith &amp;<br>Focus</h2>
  <p class="caption">Give your child a<br>great start!</p>
  <div class="brand-box"><span class="wordmark-dot"></span><span class="wordmark">Kestrel Ridge<br>Christian College</span></div>
</section>

<section class="ad ad--academic">
  <div class="sun-band"></div>
  <div class="photo" role="img" aria-label="Boy in glasses and a plaid shirt raising one finger, holding a book"></div>
  <h2 class="headline">Academic<br>Excellence</h2>
  <p class="caption">Not just a<br>score, but<br>a whole<br>educational<br>approach</p>
  <div class="brand-line"><span class="wordmark-dot"></span><span class="wordmark">Kestrel Ridge<br>Christian College</span></div>
</section>

<section class="ad ad--number">
  <div class="photo" role="img" aria-label="Boy in glasses and a white polo shirt holding a clipboard covered in long numbers"></div>
  <h2 class="headline">Don’t let your<br>child be just<br>a number</h2>
  <p class="caption">At Kestrel Ridge<br>your child is never<br>just a number, but<br>a valued member<br>of our community</p>
  <div class="brand-tab"><span class="wordmark-dot"></span><span class="wordmark">Kestrel Ridge<br>Christian College</span></div>
</section>

<section class="ad ad--standout">
  <div class="glow"></div>
  <div class="photo" role="img" aria-label="Smiling girl with pigtails and a pink backpack in a spotlight, in front of dark silhouettes of other children"></div>
  <h2 class="headline">Stand Out!</h2>
  <p class="caption">Encouraging Creativity</p>
  <div class="brand-tab"><span class="wordmark-dot"></span><span class="wordmark">Kestrel Ridge<br>Christian College</span></div>
</section>

</body>
</html>
```